Vice chair

I'm running for a position as vice chair this will be posted in the lunch room cafeteria in this package i posted logos, my picture, sample of old flyers to give you a idea i also wrote literature need help in putting it together like it to look like a million bucks goal win this election I summited lots of pdf files and jpeg look though them to help with your design feel free to contact me to further assist you
Updates

Would like this to be completed by Wednesday

Target Market(s)

My constituents

Font styles to use
Serif

Colors

Designer to choose colors to be used in the design.

Requirements
Must have
• Make it look clean neat
Nice to have
• Nice background

```html
<!DOCTYPE html>
<html lang="en">
<head>
<meta charset="utf-8">
<title>Vote for Marco Delgado – Vice Chair</title>
<link href="https://fonts.googleapis.com/css2?family=Montserrat:wght@700;800&family=Open+Sans:wght@400;600;700&display=swap" rel="stylesheet">
<style>
  :root{
    --navy:#1f3a8a;
    --blue:#2a4fa6;
    --red:#d7204f;
    --pink:#e8456f;
    --ink:#2a2a2a;
    --paper:#ffffff;
    --mist:#eef0f4;
    --gold:#e0a12a;
    --green:#3aa845;
    --bg:#dcdde0;
  }
  *{box-sizing:border-box;margin:0;padding:0}
  html,body{width:1200px;height:986px;overflow:hidden;background:var(--bg)}
  .flyer{position:relative;width:1200px;height:986px;background:var(--paper);overflow:hidden;font-family:"Open Sans",Arial,sans-serif;color:var(--ink)}
  .hero{position:absolute;left:0;top:0;width:1200px;height:470px}
  .hero-flag{position:absolute;inset:0;background:linear-gradient(160deg,#dfe2ea 0%,#c9ccd8 30%,#e7d2d6 55%,#b96f7c 75%,#e9e4e6 100%)}
  .hero-photo{position:absolute;left:120px;top:60px;width:380px;height:380px;border-radius:46% 46% 0 0;background:linear-gradient(180deg,#7a5a4a 0%,#5a4036 60%,#1e2233 100%)}
  .hero-band{position:absolute;left:0;top:0;width:1200px;height:470px}
  .headline{position:absolute;left:560px;top:60px;width:600px}
  .headline-respect{font-family:"Montserrat",Arial,sans-serif;font-weight:800;font-size:66px;line-height:1;color:var(--navy)}
  .headline-respect span{color:var(--red)}
  .headline-integrity{font-family:"Montserrat",Arial,sans-serif;font-weight:800;font-size:66px;line-height:1;color:var(--red)}
  .headline-union{font-family:"Montserrat",Arial,sans-serif;font-weight:700;font-size:22px;color:var(--navy);margin-top:8px;letter-spacing:.5px}
  .headline-tag{font-weight:700;font-size:16px;color:#111}
  .faint-stars{position:absolute;left:0;top:470px;width:600px;height:360px;opacity:.5}
  .brand{position:absolute;left:60px;top:495px;display:flex;align-items:center;gap:12px}
  .brand-dot{width:60px;height:60px;border-radius:50%;background:var(--gold)}
  .brand-name{font-family:"Montserrat",Arial,sans-serif;font-weight:800;font-size:20px;line-height:1.05;color:var(--green);width:170px}
  .vote{position:absolute;left:60px;top:580px}
  .vote-for{font-family:"Montserrat",Arial,sans-serif;font-weight:800;font-size:42px;color:var(--blue);line-height:1}
  .vote-name{font-family:"Montserrat",Arial,sans-serif;font-weight:800;font-size:50px;color:var(--red);line-height:1.05}
  .intro{position:absolute;left:60px;top:692px;width:520px;font-size:15px;line-height:1.28;text-align:justify}
  .intro p+p{margin-top:12px}
  .points{position:absolute;left:650px;top:500px;width:500px;list-style:none;font-size:15.5px;line-height:1.3}
  .points li{position:relative;padding-left:30px;margin-bottom:14px}
  .points li::before{content:"★";position:absolute;left:0;top:0;color:var(--navy);font-size:18px}
  .points li:nth-child(even)::before{color:var(--red)}
  .badges{position:absolute;left:760px;top:790px;display:flex;gap:60px;align-items:flex-end}
  .badge{width:100px;height:100px;border-radius:50%;border:4px solid #fff;box-shadow:0 0 0 2px #999}
  .badge-blue{background:var(--blue)}
  .badge-orange{background:#f07a1a}
  .badge-yellow{background:#f5d90a}
  .footer{position:absolute;left:0;bottom:0;width:1200px;height:60px}
</style>
</head>
<body>
<main class="flyer">
  <section class="hero">
    <div class="hero-flag" role="img" aria-label="Waving American flag background"></div>
    <div class="hero-photo" role="img" aria-label="Portrait photo of the candidate"></div>
    <svg class="hero-band" viewBox="0 0 1200 470" aria-hidden="true">
      <polygon points="0,470 0,390 600,440 1200,250 1200,470" fill="#fff"/>
      <polygon points="0,370 600,420 1200,230 1200,300 600,462 0,412" fill="var(--red)"/>
      <polygon points="0,330 600,380 1200,150 1200,240 600,430 0,380" fill="var(--navy)"/>
      <g fill="#fff" font-size="34" font-family="Arial" text-anchor="middle">
        <text x="90" y="376">★</text><text x="250" y="390">★</text><text x="410" y="403">★</text><text x="570" y="416">★</text>
        <text x="720" y="380">★</text><text x="870" y="326">★</text><text x="1020" y="270">★</text><text x="1160" y="218">★</text>
      </g>
    </svg>
    <div class="headline">
      <div class="headline-respect">RESPECT <span>&amp;</span></div>
      <div class="headline-integrity">INTERGRITY</div>
      <div class="headline-union">TRANSIT CREW ALLIANCE</div>
      <div class="headline-tag">Will be the Backbone that Shapes Our Union</div>
    </div>
  </section>

  <svg class="faint-stars" viewBox="0 0 600 360" aria-hidden="true">
    <g fill="var(--mist)" font-size="70" font-family="Arial">
      <text x="20" y="90">★</text><text x="130" y="60">★</text><text x="360" y="200">★</text><text x="470" y="320">★</text><text x="60" y="300">★</text>
    </g>
  </svg>

  <div class="brand">
    <span class="brand-dot"></span>
    <span class="brand-name">TRANSIT CREW ALLIANCE</span>
  </div>

  <div class="vote">
    <div class="vote-for">VOTE FOR</div>
    <div class="vote-name">MARCO DELGADO</div>
  </div>

  <div class="intro">
    <p>I Marco Delgado for those who don't know me would like to introduce myself I have always been approachable and helpful whether you are a probationary officer or a veteran operator with knowledge or information. We must protect our union rules for ourselves our future and most important our</p>
    <p>I would like this opportunity to run as your vice chair a person you can trust and believe in me Positive and motivations are my main keys for progress and for change in my campaign When there are no leaders to look up to one therefore must become one I do believe I'm the right person for this position so please come out and support me and vote me as your vice chair</p>
  </div>

  <ul class="points">
    <li>20 years on the job</li>
    <li>Past union member of Freight Haulers local 295 believes in There is a collective bargaining agreement in place and no management is above the law to violate it</li>
    <li>Past union member of Freight Haulers local 851 believes a house that is divided cannot stand</li>
    <li>In closing I believe that our union does not stand out individually achievement we must stand for collective advancement for all. we must always continue to stand together, stay together &amp; fight together so we can win together because success is never owned, it is rented and the rent is due every day.</li>
  </ul>

  <div class="badges">
    <span class="badge badge-blue"></span>
    <span class="badge badge-orange"></span>
    <span class="badge badge-yellow"></span>
  </div>

  <svg class="footer" viewBox="0 0 1200 60" aria-hidden="true">
    <polygon points="0,38 1200,10 1200,60 0,60" fill="var(--pink)"/>
    <polyline points="0,31 1200,3" stroke="var(--navy)" stroke-width="3" fill="none"/>
  </svg>
</main>
</body>
</html>
```